Harbor Business Cards

I need a business card designed with the following information.

Company Name: Harbor Wealth Management
Name: BriAnne Dockery
Title: Executive Assistant
Cell: (555) 210-0173
Direct Line: (555) 320-0148
Email: brianne@harborwmx.com
Address: 20537 W. Marlowe PKWY Ste. B
Alderport, OR 97390

I have attached the logo.
I would like it in navy blue and silver.
Thanks.

```html
<!DOCTYPE html>
<html lang="en">
<head>
<meta charset="utf-8">
<title>Harbor Wealth Management – Business Card</title>
<link href="https://fonts.googleapis.com/css2?family=Questrial&display=swap" rel="stylesheet">
<style>
  :root {
    --navy: #13223f;
    --white: #ffffff;
    --silver: #c9ccd2;
    --backdrop: #9dd6cb;
  }
  * { box-sizing: border-box; margin: 0; padding: 0; }
  html, body { width: 1200px; height: 1200px; overflow: hidden; }
  body {
    background: var(--backdrop);
    font-family: "Questrial", "Century Gothic", sans-serif;
    position: relative;
  }
  .card {
    position: absolute;
    left: 250px;
    width: 700px;
    height: 400px;
    background: var(--white);
    box-shadow: 0 6px 18px rgba(0, 0, 0, 0.15);
    overflow: hidden;
  }
  .card--back { top: 160px; }
  .card--front { top: 640px; }

  .wordmark { color: var(--navy); text-align: center; line-height: 1; }
  .wordmark__name { font-size: 34px; letter-spacing: 14px; padding-left: 14px; }
  .wordmark__sub { font-size: 11px; letter-spacing: 5px; padding-left: 5px; margin-top: 8px; }

  .card--back .wordmark { position: absolute; top: 120px; left: 0; right: 0; }
  .card--back .web-band {
    position: absolute; left: 0; right: 0; top: 262px; height: 78px;
    background: var(--navy); color: var(--white);
    display: flex; align-items: center; justify-content: center;
    font-size: 26px; letter-spacing: 1px;
  }

  .card--front .wordmark { position: absolute; top: 38px; left: 44px; text-align: left; }
  .card--front .wordmark__name { font-size: 26px; letter-spacing: 10px; padding-left: 0; }
  .card--front .wordmark__sub { font-size: 9px; letter-spacing: 4px; padding-left: 0; margin-top: 6px; }

  .contact-band {
    position: absolute; left: 0; right: 0; top: 132px; bottom: 0;
    background: var(--navy); color: var(--white);
  }
  .contact-list { position: absolute; left: 34px; top: 30px; list-style: none; font-size: 21px; line-height: 30px; }
  .contact-list li { display: flex; align-items: center; gap: 8px; }
  .contact-list .icon { width: 22px; height: 22px; flex: none; }
  .contact-list .no-icon { padding-left: 30px; }

  .person { position: absolute; right: 40px; top: 92px; text-align: right; }
  .person__name {
    font-size: 26px; letter-spacing: 0.5px;
    border-bottom: 2px solid var(--silver); padding-bottom: 2px;
  }
  .person__title { font-size: 11px; letter-spacing: 1px; margin-top: 4px; color: var(--silver); }

  .band-mark {
    position: absolute; right: 42px; bottom: 30px;
    font-size: 22px; letter-spacing: 6px; color: var(--white);
  }
</style>
</head>
<body>

<section class="card card--back" aria-label="Card back">
  <div class="wordmark">
    <div class="wordmark__name">HARBOR</div>
    <div class="wordmark__sub">WEALTH MANAGEMENT</div>
  </div>
  <div class="web-band">www.briannharborwmx.com</div>
</section>

<section class="card card--front" aria-label="Card front">
  <div class="wordmark">
    <div class="wordmark__name">HARBOR</div>
    <div class="wordmark__sub">WEALTH MANAGEMENT</div>
  </div>

  <div class="contact-band">
    <ul class="contact-list">
      <li>
        <svg class="icon" viewBox="0 0 24 24" aria-hidden="true"><circle cx="12" cy="12" r="12" fill="#fff"/><path d="M8 6.5c.6-.4 1.2-.3 1.5.2l1.2 2c.3.5.2 1-.2 1.3l-.8.6c.6 1.4 1.6 2.5 3 3.2l.6-.8c.3-.4.9-.5 1.3-.2l2 1.2c.5.3.6.9.2 1.5-.8 1-2 1.4-3.2.9-2.8-1.2-4.8-3.2-6-6-.5-1.2-.3-2.3.4-3.9z" fill="var(--navy)"/></svg>
        <span>(555) 210-0173</span>
      </li>
      <li>
        <svg class="icon" viewBox="0 0 24 24" aria-hidden="true"><circle cx="12" cy="12" r="12" fill="#fff"/><rect x="9" y="5.5" width="6" height="13" rx="1.2" fill="var(--navy)"/><rect x="10" y="7" width="4" height="9" fill="#fff"/></svg>
        <span>(555) 320-0148</span>
      </li>
      <li>
        <svg class="icon" viewBox="0 0 24 24" aria-hidden="true"><circle cx="12" cy="12" r="12" fill="#fff"/><rect x="6" y="8" width="12" height="8" rx="1" fill="var(--navy)"/><path d="M6.5 8.5 12 12.5l5.5-4" stroke="#fff" stroke-width="1.2" fill="none"/></svg>
        <span>brianne@harborwmx.com</span>
      </li>
      <li>
        <svg class="icon" viewBox="0 0 24 24" aria-hidden="true"><circle cx="12" cy="12" r="12" fill="#fff"/><path d="M12 5.5 5.5 11.5h2v6h3.5v-4h2v4h3.5v-6h2z" fill="var(--navy)"/></svg>
        <span>20537 W. Marlowe PKWY Ste. B</span>
      </li>
      <li class="no-icon">Alderport, OR 97390</li>
    </ul>

    <div class="person">
      <div class="person__name">BRIANNE DOCKERY</div>
      <div class="person__title">EXECUTIVE ASSISTANT</div>
    </div>

    <div class="band-mark">HARBOR</div>
  </div>
</section>

</body>
</html>
```